KTR Motorhaus Automotive Repair and Service Shop

I need an informative and interactive website for my automotive service and repair shop. The website must give information about the shop, as well as the ability to make bookings and a forums page for our users to use and set up an account with us, in which we can give promotions via email. We are located in Pompano Beach Florida and our company name is KTR Motorhaus. Our color scheme is a red for accent and grey (neutral color) as a base. The design must communicate our message and be able to grow should we decide to retail parts in the future. One of the websites I take the highest inspiration from is http://www.lanvexbodyshop.example/. Although I do not have as nearly as many certifications as them. Attached are some images of our shop so you can see how clean and modern our building is, and I would like our website to match our feel. Thank you.

Target Market(s)

Automotive Enthusiasts

Industry/Entity Type

Automotive

Contact Information for Business Card

KTR Motorhaus /954 718 6402 /rohan@ktrmotorhaus.example/ 512 NE 9th St Pompano Beach FL 33062/ any other info needed please ask me

Coding

Coded - Design and coding required

Number of Pages Required

5+ page

Font styles to use
Sans Serif

Requirements
Must have
• Name, logo, contact info, location, phone number
Nice to have
• Building is very modern, would like a business card to match
Should not have
• Not to playful or vibrant

```html
<!DOCTYPE html>
<html lang="en">
<head>
<meta charset="utf-8">
<title>KTR Motorhaus — About Us</title>
<link rel="stylesheet" href="https://fonts.googleapis.com/css2?family=Jost:wght@400;500;600;700&display=swap">
<style>
  :root {
    --accent-red: #dc0a0a;
    --ink: #111111;
    --paper: #ffffff;
    --numeral-grey: #dedede;
    --photo-dark: #1c1a17;
    --photo-mid: #5b4e38;
    --photo-light: #a89a80;
  }
  * { margin: 0; padding: 0; box-sizing: border-box; }
  html, body { width: 1200px; height: 676px; overflow: hidden; background: var(--paper); }
  body { font-family: "Jost", sans-serif; color: var(--ink); position: relative; }

  .sidebar {
    position: absolute; left: 0; top: 0; width: 90px; height: 676px;
    background: var(--accent-red);
  }
  .brand {
    position: absolute; left: 9px; top: 22px; width: 72px;
    color: var(--paper); font-weight: 700; font-size: 10px; line-height: 1.1;
    letter-spacing: 0.04em; text-transform: uppercase; text-align: center;
  }
  .nav-link {
    position: absolute; left: 37px;
    writing-mode: vertical-rl;
    font-family: "Jost", sans-serif; font-weight: 500; font-size: 9.5px;
    letter-spacing: 0.06em; color: rgba(255,255,255,0.75);
    text-decoration: none;
  }
  .nav-link.is-active {
    color: var(--paper);
    border-right: 3px solid var(--ink);
    background: linear-gradient(to left, var(--ink) 0 3px, transparent 3px);
    padding: 2px 0;
  }

  .section-numeral { position: absolute; left: 156px; top: 56px; }

  .about {
    position: absolute; left: 259px; top: 186px; width: 280px;
  }
  .about-title {
    color: var(--accent-red); font-weight: 600; font-size: 45px;
    letter-spacing: 0.03em; line-height: 1;
  }
  .about-lead {
    margin-top: 26px; font-weight: 600; font-size: 13.6px; line-height: 15.6px;
  }
  .about-body {
    margin-top: 12px; font-weight: 400; font-size: 13.6px; line-height: 15.8px;
    letter-spacing: 0.02em;
  }
  .learn-more {
    display: inline-block; margin-top: 12px;
    color: var(--accent-red); font-weight: 600; font-size: 13.6px;
    text-decoration: none; letter-spacing: 0.02em;
  }

  .engine-photo {
    position: absolute; left: 696px; top: 56px; width: 504px; height: 552px;
    background:
      radial-gradient(ellipse at 55% 45%, var(--photo-light) 0%, var(--photo-mid) 35%, transparent 70%),
      linear-gradient(135deg, var(--photo-dark) 0%, var(--photo-mid) 50%, var(--photo-dark) 100%);
  }
</style>
</head>
<body>
  <nav class="sidebar">
    <div class="brand">KTR Motorhaus</div>
    <a class="nav-link" href="#" style="top:121px">Main Page</a>
    <a class="nav-link is-active" href="#" style="top:233px">About Us</a>
    <a class="nav-link" href="#" style="top:340px">Our Services</a>
    <a class="nav-link" href="#" style="top:465px">Cars</a>
    <a class="nav-link" href="#" style="top:544px">Contacts</a>
  </nav>

  <svg class="section-numeral" width="350" height="210" viewBox="0 0 350 210" aria-hidden="true">
    <circle cx="103" cy="103" r="83" fill="none" stroke="var(--numeral-grey)" stroke-width="41"/>
    <line x1="50" y1="150" x2="152" y2="52" stroke="var(--numeral-grey)" stroke-width="30"/>
    <polygon points="281,6 320,6 320,160 281,160 281,82 250,70" fill="var(--numeral-grey)"/>
    <rect x="244" y="160" width="106" height="40" fill="var(--numeral-grey)"/>
  </svg>

  <main class="about">
    <h1 class="about-title">About Us</h1>
    <p class="about-lead">Lorem ipsum dolor sit amet, consectetur adipiscing aliqua.</p>
    <p class="about-body">Lorem ipsum dolor sit amet, consectetur adipiscing elit, sed do eiusmod tempor incididunt ut labore et dolore magna aliqua. Duis aute irure dolor in reprehenderit in voluptate velit esse cillum dolore eu fugiat nulla pariatur. Excepteur sint occaecat cupidatat non proident, sunt in culpa qui officia deserunt mollit anim id est laborum.</p>
    <a class="learn-more" href="#">Learn More</a>
  </main>

  <div class="engine-photo" role="img" aria-label="Close-up photo of an engine's camshafts and timing chain"></div>
</body>
</html>
```